BRIGHTDESK - Remote Tech Support Site

We are looking for a new very responsive and simple website for our brand Brightdesk.com - a remote technical support company.

This company supports customers Globally in different countries throughout Eur/ North America / South America / Asia etc (please keep this in mind and integrate into the idea).

Its important to us that the design is very explanatory, the customer should easily be able to figure out that we provide computer support right away ... I like one page responsive type designs as well without a bunch of menu items

Here are some similar sites we like - but still looking for a unique design that fits out brand "brightdesk" - I have upload also some layouts i like (but the designs are not important just the layouts), youll see it includes consumer business etc which is important.

VOLM.COM - I love how clean it is - nice and white easy to see everything

PLUMWIRE247.COM - also nice the layout and responsive one page design makes it easy to use

corvalfix.com - similar to plumwire design as well - you can get the idea im looking for between the two

You will notice those examples are much different then the attachments I added - again this is more of an idea for possible layouts .. attached is also the logo - could inspire color scheme / blue white black etc

Target Market(s)

Home consumers without computer knowledge , older age 45-65, small medium business ... computer repair - slow computers

Industry/Entity Type

Computer Repair

Logo Text

Brightdesk

Coding

Coded - Design and coding required

Number of Pages Required

1 page

Font styles to use
Sans Serif
Other font styles liked:
• your choice responsive

Colors

Designer to choose colors to be used in the design.

Requirements
Must have
• Clean - responsive - professional design - the name says it all - brightdesk
• CALL TO ACTIONS FOR "Get Help Now!" / "Learn More" etc
Nice to have
• We are looking for a new very responsive and simple website for our brand Brightdesk.com - a remote technical support company.
• This company supports customers Globally in different countries throughout Eur/ North America / South America / Asia etc (please keep this in mind and integrate into the idea).
• Its important to us that the design is very explanatory, the customer should easily be able to figure out that we provide computer support right away ... I like one page responsive type designs as well without a bunch of menu items
• Here are some similar sites we like - but still looking for a unique design that fits out brand "brightdesk" - I have upload also some layouts i like (but the designs are not important just the layouts), youll see it includes consumer business etc which is important.
• VOLM.COM - I love how clean it is - nice and white easy to see everything
• PLUMWIRE247.COM - also nice the layout and responsive one page design makes it easy to use
• corvalfix.com - similar to plumwire design as well - you can get the idea im looking for between the two
Should not have
• dark, packed page - bad small font -

```html
<!DOCTYPE html>
<html lang="en">
<head>
<meta charset="utf-8">
<title>Brightdesk – Dedicated Support Anytime, Anywhere</title>
<link rel="stylesheet" href="https://fonts.googleapis.com/css2?family=Open+Sans:ital,wght@0,400;0,600;0,700;0,800;1,400;1,700&display=swap">
<style>
:root{
  --blue:#2a8df0;
  --blue-dark:#1f74d0;
  --blue-soft:#4ea3f5;
  --ink:#1d1d1f;
  --grey-text:#555a60;
  --card-head:#2e3033;
  --panel:#f2f3f5;
  --line:#cfd6de;
  --white:#ffffff;
  --footer-bg:#ffffff;
  --copy-bg:#ececec;
}
*{margin:0;padding:0;box-sizing:border-box}
html,body{width:1200px;height:3495px;overflow:hidden}
body{position:relative;font-family:"Open Sans",Arial,sans-serif;color:var(--ink);background:var(--white)}
.abs{position:absolute}
a{color:inherit;text-decoration:none}

/* top strip */
.top-rule{left:0;top:0;width:1200px;height:8px;background:var(--blue)}
.hero-photo{left:0;top:8px;width:1200px;height:700px;background:linear-gradient(100deg,#f6f7f9 0%,#eef0f2 30%,#ddd8d3 58%,#c9c2bb 78%,#e7e3df 100%)}
.utility{right:38px;top:22px;display:flex;align-items:center;gap:16px;font-size:16px;font-weight:700;color:var(--blue)}
.utility .socials{display:flex;gap:5px}
.utility .socials span{width:22px;height:22px;border:2px solid var(--blue);border-radius:50%}
.utility .lang{font-size:14px}
.utility .sep{width:2px;height:16px;background:var(--blue)}

/* nav */
.brand{display:flex;align-items:center;gap:10px;font-weight:700;color:var(--blue-dark)}
.brand .dot{border-radius:50%;background:var(--blue)}
.header-brand{left:42px;top:74px;font-size:38px}
.header-brand .dot{width:48px;height:48px}
.nav{left:530px;top:84px;display:flex;align-items:center;gap:26px;font-size:15px;font-weight:700;color:var(--ink)}
.nav .globe{width:28px;height:28px}
.chat-btn{left:955px;top:82px;width:202px;height:36px;border:2px solid var(--blue);border-radius:8px;background:var(--blue);color:var(--white);font-size:14px;font-weight:700;display:flex;align-items:center;justify-content:center;gap:10px}
.chat-btn .bubble{width:34px;height:22px;background:var(--white);border-radius:11px}

/* hero copy */
.hero-title{left:60px;top:258px;line-height:1.15}
.hero-title .lead{font-size:47px;font-weight:700;color:var(--blue);display:block}
.hero-title .sub{font-size:45px;font-weight:800;color:var(--ink);display:block}
.btn-primary{background:var(--blue);color:var(--white);font-weight:700;border-radius:12px;display:flex;align-items:center;justify-content:center;box-shadow:0 6px 14px rgba(20,90,170,.25)}
.hero-cta{left:98px;top:396px;width:342px;height:66px;font-size:30px}

/* pricing */
.price-band{left:0;top:690px;width:1200px;height:310px}
.plan{top:630px;width:322px;height:325px;background:var(--white);border-radius:8px;box-shadow:0 4px 12px rgba(0,0,0,.18);overflow:visible}
.plan-head{height:46px;background:var(--card-head);color:var(--white);font-weight:700;font-size:17px;display:flex;align-items:center;justify-content:center;border-radius:8px 8px 0 0;letter-spacing:.5px}
.plan-price{text-align:center;margin-top:22px;color:var(--blue);font-weight:800;font-style:italic;font-size:36px;line-height:1}
.plan-price small{font-size:15px;font-weight:700}
.plan-fee{text-align:center;font-size:13px;font-weight:600;color:var(--grey-text);margin-top:6px}
.plan-list{margin:16px 16px 0;background:var(--panel);height:112px;display:flex;flex-direction:column;justify-content:center;text-align:center;font-size:15.5px;line-height:1.35;color:var(--grey-text)}
.plan-list b{color:var(--ink);font-weight:700}
.plan-btn{position:absolute;left:28px;bottom:-16px;width:266px;height:40px;background:var(--blue);border-radius:6px;color:var(--white);font-weight:700;font-size:15px;display:flex;align-items:center;justify-content:center;padding-left:48px}
.plan-btn .mark{position:absolute;left:-14px;top:-10px;width:60px;height:60px;border-radius:50%;background:var(--white);box-shadow:0 2px 6px rgba(0,0,0,.2);display:flex;align-items:center;justify-content:center}
.plan-btn .mark i{width:34px;height:34px;border-radius:50%;background:var(--blue)}
.popular{left:1058px;top:598px;width:106px;height:106px;border-radius:50%;background:var(--blue);border:5px solid var(--white);color:var(--white);font-weight:800;font-style:italic;font-size:17px;line-height:1.1;display:flex;align-items:center;justify-content:center;text-align:center}

/* section titles */
.section-title{left:0;width:1200px;display:flex;align-items:center;justify-content:center;gap:12px;font-weight:800;font-size:23px}
.section-title .rule{width:120px;height:1px;background:var(--line)}
.section-title .dot{width:34px;height:34px;border-radius:50%;background:var(--blue)}
.section-title .hl{color:var(--blue)}
.features-title{top:1068px}

/* features */
.feature{width:250px}
.feature svg{display:block;width:90px;height:90px;margin-left:18px}
.feature h3{color:var(--blue);font-size:18px;font-weight:700;margin-top:10px}
.feature p{font-size:16px;line-height:1.2;color:var(--grey-text)}
.feature.centered{text-align:center;width:240px}
.feature.centered svg{margin:0 auto}
.feature-cta{left:485px;top:1600px;width:228px;height:57px;font-size:24px;border-radius:10px}

/* how it works */
.how-band{left:0;top:1701px;width:1200px;height:510px}
.how-title{top:1782px;color:var(--white);font-size:22px}
.how-title .rule{background:rgba(255,255,255,.8)}
.how-title .dot{background:var(--white)}
.step{top:1862px;width:300px;color:var(--white)}
.step svg{display:block;width:100px;height:86px;margin-bottom:16px}
.step h3{font-size:19px;font-weight:700}
.step p{font-size:16.5px;line-height:1.22;opacity:.95}
.how-cta{left:485px;top:2100px;width:228px;height:54px;font-size:24px;border-radius:10px;background:var(--white);color:var(--blue-dark)}

/* testimonial */
.quote-box{left:256px;top:2286px;width:690px;height:136px;border:2px solid #b9d3ee;border-radius:6px;background:var(--white);padding:18px 26px 0 62px;font-size:13.5px;line-height:1.35;color:var(--grey-text);box-shadow:0 2px 6px rgba(0,0,0,.06)}
.quote-box .qmark{position:absolute;left:20px;top:12px;font-size:52px;font-weight:800;color:var(--ink);line-height:1}
.quote-box::after{content:"";position:absolute;left:40px;bottom:-14px;width:24px;height:24px;background:var(--white);border-right:2px solid #b9d3ee;border-bottom:2px solid #b9d3ee;transform:rotate(45deg)}
.quote-name{left:256px;top:2444px;font-size:17px;font-weight:700;font-style:italic}
.dots{left:568px;top:2488px;display:flex;gap:6px}
.dots span{width:12px;height:12px;border-radius:50%;border:2px solid #9aa6b2}
.dots span.on{background:var(--blue);border-color:var(--blue)}

/* video */
.video-band{left:0;top:2540px;width:1200px;height:500px}
.video-line{left:0;top:2688px;width:1200px;display:flex;align-items:center;justify-content:center;gap:16px;color:var(--white);font-weight:700;font-size:34px}
.video-line .brand{color:var(--white);font-size:40px}
.video-line .brand .dot{width:52px;height:52px;background:var(--white)}
.play{left:538px;top:2780px;width:126px;height:126px;border-radius:50%;background:rgba(255,255,255,.92);display:flex;align-items:center;justify-content:center}

/* footer */
.footer-brand{left:42px;top:3106px;font-size:32px}
.footer-brand .dot{width:42px;height:42px}
.footer-socials{left:116px;top:3180px;display:flex;gap:5px}
.footer-socials span{width:24px;height:24px;border:2px solid #6a7078;border-radius:50%}
.foot-col{top:3106px}
.foot-col h4{color:var(--blue);font-size:15px;font-weight:800;padding-bottom:10px;border-bottom:1px solid var(--line);margin-bottom:12px;width:160px}
.foot-col li{list-style:none;font-size:13px;line-height:19.6px;color:var(--ink)}
.newsletter input{display:block;width:184px;height:28px;border:1px solid #9aa2aa;font-size:10px;padding:0 8px;font-family:inherit}
.newsletter .sign{display:inline-block;margin-top:8px;background:var(--card-head);color:var(--white);font-size:12px;font-weight:700;padding:6px 16px}
.contact-box{left:885px;top:3104px;width:276px;height:178px;background:var(--blue);border-radius:4px;color:var(--white);text-align:center;padding-top:20px}
.contact-box h4{font-size:16px;font-weight:800}
.contact-box .phone{display:flex;align-items:center;justify-content:center;gap:10px;font-size:27px;font-weight:700;margin-top:2px}
.contact-box .btn-line{margin:22px auto 0;width:180px;height:40px;border:2px solid var(--white);border-radius:6px;font-weight:800;font-size:17px;display:flex;align-items:center;justify-content:center}
.badge{top:3300px}
.copyright{left:0;top:3450px;width:1200px;height:45px;background:var(--copy-bg);font-size:11px;font-weight:600;display:flex;align-items:center;justify-content:center;color:#444}
</style>
</head>
<body>

<div class="abs top-rule"></div>
<div class="abs hero-photo" role="img" aria-label="Photo of a smiling older couple looking at a laptop together at home"></div>

<div class="abs utility">
  <span>
    <svg width="20" height="20" viewBox="0 0 24 24" style="vertical-align:-4px"><circle cx="12" cy="12" r="11" fill="none" stroke="currentColor" stroke-width="2"/><path d="M8 6c1 0 2 2 2 3s-1 1-1 2 3 4 4 4 1-1 2-1 3 1 3 2-1 2-2 2C11 18 6 13 6 8c0-1 1-2 2-2z" fill="currentColor"/></svg>
    (888) 555-0142
  </span>
  <span class="socials"><span></span><span></span><span></span></span>
  <span class="lang">United States - EN ▾</span>
  <span class="sep"></span>
  <span>LOGIN</span>
</div>

<div class="abs brand header-brand"><span class="dot"></span>brightdesk</div>

<nav class="abs nav">
  <svg class="globe" viewBox="0 0 28 28"><circle cx="14" cy="14" r="13" fill="var(--blue)"/><circle cx="14" cy="14" r="8" fill="none" stroke="#fff" stroke-width="1.6"/><path d="M6 14h16M14 6c-3 3-3 13 0 16M14 6c3 3 3 13 0 16" fill="none" stroke="#fff" stroke-width="1.4"/></svg>
  <a>ABOUT</a><a>SERVICES</a><a>FAQS</a><a>CONTACT</a>
</nav>
<div class="abs chat-btn"><span class="bubble"></span>CHAT WITH US</div>

<h1 class="abs hero-title"><span class="lead">Dedicated Support</span><span class="sub">Anytime. Anywhere.</span></h1>
<a class="abs btn-primary hero-cta">GET HELP NOW!</a>

<!-- pricing band -->
<svg class="abs price-band" viewBox="0 0 1200 310" preserveAspectRatio="none"><path d="M0 0H1200V262C900 300 700 300 600 282S250 250 0 298Z" fill="var(--blue)"/></svg>

<div class="abs plan" style="left:75px">
  <div class="plan-head">PREMIUM</div>
  <div class="plan-price">$19.99<small>/MONTHLY</small></div>
  <div class="plan-fee">($249-$300 setup fee)</div>
  <div class="plan-list"><span>Regular 90-Day Optimization</span><b>Unlimited 24/7 Tier 3</b><b>Technician Support</b></div>
  <a class="plan-btn"><span class="mark"><i></i></span>SIGN UP NOW</a>
</div>
<div class="abs plan" style="left:438px">
  <div class="plan-head">PREMIUM PLUS</div>
  <div class="plan-price">$29.99<small>/MONTHLY</small></div>
  <div class="plan-fee">($249-$300 setup fee)</div>
  <div class="plan-list"><span>Regular 90-Day Optimization</span><b>Unlimited 24/7 Tier 3</b><b>Technician Support</b></div>
  <a class="plan-btn"><span class="mark"><i></i></span>SIGN UP NOW</a>
</div>
<div class="abs plan" style="left:804px">
  <div class="plan-head">PLATINUM</div>
  <div class="plan-price">$39.99<small>/MONTHLY</small></div>
  <div class="plan-fee">($249-$300 setup fee)</div>
  <div class="plan-list"><span>Regular 90-Day Optimization</span><b>Unlimited 24/7 Tier 3</b><b>Technician Support</b><b>Online Identity Theft Protection</b></div>
  <a class="plan-btn"><span class="mark"><i></i></span>SIGN UP NOW</a>
</div>
<div class="abs popular">MOST<br>POPULAR</div>

<!-- features -->
<h2 class="abs section-title features-title"><span class="rule"></span><span class="dot"></span>ALL THE BEST FEATURES,&nbsp;<span class="hl">AT THE BEST PRICE!</span><span class="rule"></span></h2>

<div class="abs feature" style="left:82px;top:1142px">
  <svg viewBox="0 0 90 90" fill="none" stroke="#333" stroke-width="3"><circle cx="45" cy="45" r="38"/><path d="M18 18l54 54"/><rect x="28" y="34" width="34" height="22" rx="3"/></svg>
  <h3>Ad Blocker</h3><p>Avoid unwanted Pop-ups with the newest Ad Blocking technology.</p>
</div>
<div class="abs feature" style="left:361px;top:1142px">
  <svg viewBox="0 0 90 90" fill="none" stroke="#333" stroke-width="3"><rect x="20" y="24" width="56" height="38" rx="3"/><path d="M12 68h72"/><circle cx="22" cy="20" r="9" stroke-dasharray="4 3"/><circle cx="22" cy="20" r="3"/></svg>
  <h3>Regular Tune-Ups</h3><p>Get a Regular Tune-Up and Optimization every 90 days.</p>
</div>
<div class="abs feature" style="left:645px;top:1142px">
  <svg viewBox="0 0 90 90" fill="none" stroke="#333" stroke-width="3"><rect x="16" y="10" width="54" height="70" rx="3"/><path d="M16 22h54M26 36h34M26 46h20"/><path d="M48 70a14 14 0 1 1 14-14H48z" fill="#333"/></svg>
  <h3>System Reports</h3><p>Stay up to date with Real-Time System Reporting.</p>
</div>
<div class="abs feature" style="left:927px;top:1142px">
  <svg viewBox="0 0 90 90" fill="none" stroke="#333" stroke-width="3"><rect x="10" y="12" width="40" height="28" rx="2"/><rect x="40" y="44" width="42" height="30" rx="2"/><path d="M24 40v10h16M60 74v8M52 82h18"/></svg>
  <h3>Multiple Devices</h3><p>Get support for up to 4 multiple devices. Ask about our Family Plans.</p>
</div>

<div class="abs feature centered" style="left:45px;top:1372px">
  <svg viewBox="0 0 90 90" fill="none" stroke="#333" stroke-width="3"><rect x="12" y="12" width="66" height="50" rx="3"/><path d="M12 24h66M18 70h54"/><rect x="34" y="38" width="22" height="18" rx="2"/><path d="M38 38v-6a7 7 0 0 1 14 0v6"/></svg>
  <h3>Identity Protection</h3>
</div>
<div class="abs feature centered" style="left:320px;top:1372px">
  <svg viewBox="0 0 90 90" fill="none" stroke="#333" stroke-width="3"><rect x="26" y="6" width="38" height="76" rx="5"/><path d="M26 18h38M26 68h38"/><path d="M45 30l10 4v8c0 6-5 9-10 11-5-2-10-5-10-11v-8z"/></svg>
  <h3>Mobile Security</h3>
</div>
<div class="abs feature" style="left:630px;top:1372px">
  <svg viewBox="0 0 90 90" fill="none" stroke="#333" stroke-width="3"><rect x="18" y="8" width="54" height="60" rx="3"/><path d="M28 22h34M28 32h34M28 42h24"/><path d="M10 82c4-10 14-16 26-16h20" stroke-width="5"/></svg>
  <h3>Cross Platform Support</h3><p>One Support Plan for different types of devices.</p>
</div>
<div class="abs feature" style="left:912px;top:1372px">
  <svg viewBox="0 0 90 90" fill="none" stroke="#333" stroke-width="3"><path d="M24 62h44a14 14 0 0 0 0-28 22 22 0 0 0-42-4 16 16 0 0 0-2 32z"/><path d="M34 46a12 12 0 0 1 22-4M56 36v6h-6M56 50a12 12 0 0 1-22 4M34 60v-6h6"/></svg>
  <h3>Cloud Backup</h3><p>Keep your data safe! Ask about our plans for Unlimited Cloud Backup.</p>
</div>

<a class="abs btn-primary feature-cta">Get Help Now!</a>

<!-- how it works -->
<svg class="abs how-band" viewBox="0 0 1200 510" preserveAspectRatio="none" role="img" aria-label="Blue-tinted photo of a laptop with a data privacy screen and padlock">
  <defs><linearGradient id="howFill" x1="0" y1="0" x2="1" y2="1"><stop offset="0" stop-color="#3c97f2"/><stop offset=".55" stop-color="#2a86e8"/><stop offset="1" stop-color="#5aa8f2"/></linearGradient></defs>
  <path d="M0 14C400 -6 800 -6 1200 22V490C800 516 400 516 0 492Z" fill="url(#howFill)"/>
</svg>
<h2 class="abs section-title how-title"><span class="rule" style="width:110px"></span><span class="dot"></span>HOW IT WORKS<span class="rule" style="width:180px"></span></h2>

<div class="abs step" style="left:150px">
  <svg viewBox="0 0 100 86" fill="none" stroke="#fff" stroke-width="4"><rect x="6" y="6" width="70" height="50" rx="3"/><path d="M26 72h30M41 56v16"/><circle cx="36" cy="30" r="10"/><circle cx="70" cy="58" r="14"/><path d="M80 68l14 14"/></svg>
  <h3>FREE Diagnostic</h3><p>Get a diagnostic, FOR FREE!<br>Get a free consultation with our staff.</p>
</div>
<div class="abs step" style="left:485px">
  <svg viewBox="0 0 100 86" fill="none" stroke="#fff" stroke-width="4"><rect x="8" y="4" width="84" height="78" rx="4"/><path d="M8 18h84"/><path d="M36 70l22-22a12 12 0 0 0 16-16l-8 8-6-2-2-6 8-8a12 12 0 0 0-16 16L28 62z"/></svg>
  <h3>Get Fixed</h3><p>Get fixed, IMMEDIATELY! Our staff will solve your computer issues right before your eyes.</p>
</div>
<div class="abs step" style="left:815px">
  <svg viewBox="0 0 100 86" fill="none" stroke="#fff" stroke-width="4"><path d="M26 62H20a16 16 0 0 1 2-32 26 26 0 0 1 50 4 14 14 0 0 1 6 28h-6"/><path d="M50 78V44M38 56l12-12 12 12"/></svg>
  <h3>Backup your information!</h3><p>Saving your files is now EASY! You will be able to retain your personal files without any loss of data.</p>
</div>
<a class="abs btn-primary how-cta">Get Help Now!</a>

<!-- testimonial -->
<blockquote class="abs quote-box">
  <span class="qmark">&#8220;</span>
  Lorem ipsum dolor sit amet, consectetuer adipiscing elit, sed diam nonummy nibh euismod tincidunt ut laoreet dolore magna aliquam erat volutpat. Ut wisi enim ad minim veniam, quis nostrud exerci tation ullamcorper suscipit lobortis nisl ut aliquip ex ea commodo consequat. Duis autem vel eum iriure dolor in hendrerit in vulputate velit esse molestie consequat, vel illum dolore eu feugiat nulla facilisis at vero.
</blockquote>
<div class="abs quote-name">Daniel Reyes</div>
<div class="abs dots"><span class="on"></span><span></span><span></span><span></span></div>

<!-- video -->
<svg class="abs video-band" viewBox="0 0 1200 500" preserveAspectRatio="none" role="img" aria-label="Blue-tinted photo of hands using a tablet chart beside a laptop and coffee cup">
  <defs><linearGradient id="vidFill" x1="0" y1="0" x2="1" y2="1"><stop offset="0" stop-color="#2d86e6"/><stop offset=".5" stop-color="#3d95ee"/><stop offset="1" stop-color="#5ba9f0"/></linearGradient></defs>
  <path d="M0 0C400 20 800 20 1200 0V476C800 500 400 500 0 470Z" fill="url(#vidFill)"/>
</svg>
<div class="abs video-line">See how <span class="brand"><span class="dot"></span>brightdesk</span> works</div>
<div class="abs play"><svg width="46" height="52" viewBox="0 0 46 52"><path d="M6 4l36 22L6 48z" fill="var(--blue)"/></svg></div>

<!-- footer -->
<div class="abs brand footer-brand"><span class="dot"></span>brightdesk</div>
<div class="abs footer-socials"><span></span><span></span><span></span></div>

<div class="abs foot-col" style="left:322px">
  <h4>QUICK LINKS</h4>
  <ul><li>Home</li><li>About</li><li>Services</li><li>FAQs</li><li>Contact</li></ul>
</div>
<div class="abs foot-col" style="left:478px">
  <h4>SERVICES</h4>
  <ul><li>Updates</li><li>Networking</li><li>Optimization</li><li>Online Backup</li><li>Virus Protection</li><li>Identity Protection</li><li>Diagnosis &amp; Repair</li><li>Set-up &amp; Installation</li><li>Internet Connection</li></ul>
</div>
<div class="abs foot-col newsletter" style="left:657px">
  <h4>OUR NEWSLETTER</h4>
  <input type="text" placeholder="ENTER YOUR EMAIL ADDRESS">
  <span class="sign">SIGN UP</span>
</div>

<div class="abs contact-box">
  <h4>CONTACT US TODAY</h4>
  <div class="phone"><svg width="28" height="28" viewBox="0 0 24 24"><circle cx="12" cy="12" r="11" fill="none" stroke="#fff" stroke-width="2"/><path d="M8 6c1 0 2 2 2 3s-1 1-1 2 3 4 4 4 1-1 2-1 3 1 3 2-1 2-2 2C11 18 6 13 6 8c0-1 1-2 2-2z" fill="#fff"/></svg>(888) 555-0142</div>
  <a class="btn-line">GET HELP NOW!</a>
</div>

<div class="abs badge" style="left:678px;top:3326px;width:148px;height:48px;background:#e9ecef;border-radius:4px"></div>
<div class="abs badge" style="left:872px;top:3298px;width:100px;height:84px;background:#d8dbe0;border-radius:10px"></div>
<div class="abs badge" style="left:1040px;top:3290px;width:96px;height:96px;background:#d9b04a;border-radius:50%"></div>

<footer class="abs copyright">COPYRIGHT © 2017 BRIGHTDESK. ALL RIGHTS RESERVED.</footer>

</body>
</html>
```